Serious, modern business brochure needed for private investigator

Halloway & Partners Ltd. needs a general brochure that professionally communicates available private investigator services. The brochure will be placed on desks and lobbies. Also, will be carried into offices by hand. The brochure size is left to the designer’s discretion. The brochure needs to communicate high level of professional service provide by Halloway & Partners and also capture the high risk, fast paced, high stress, environment private investigators work in.

Industry/Entity Type

Business

Requirements
Must have
• Include provided text content
• Include Halloway & Partners logo

```html
<!DOCTYPE html>
<html lang="en">
<head>
<meta charset="utf-8">
<title>Halloway &amp; Partners Ltd. — Brochure</title>
<link href="https://fonts.googleapis.com/css2?family=Cinzel:wght@400;700&family=Open+Sans:wght@400;600;700&display=swap" rel="stylesheet">
<style>
  :root {
    --bg: #2a2a2c;
    --page-dark: #111318;
    --page-navy: #131b28;
    --red: #c41f2b;
    --red-dark: #8e141d;
    --orange: #e2601f;
    --white: #ffffff;
    --text-soft: #c9ccd2;
    --text-body: #a9adb5;
    --steel: #5d86b3;
  }
  * { box-sizing: border-box; margin: 0; padding: 0; }
  html, body { width: 857px; height: 1200px; overflow: hidden; }
  body {
    background: var(--bg);
    font-family: "Open Sans", Arial, sans-serif;
    position: relative;
  }
  .spread {
    position: absolute;
    left: 20px;
    width: 817px;
    height: 578px;
    display: flex;
    box-shadow: 0 6px 18px rgba(0,0,0,.5);
  }
  .spread--outside { top: 14px; }
  .spread--inside { top: 608px; }
  .page {
    position: relative;
    width: 50%;
    height: 100%;
    overflow: hidden;
  }
  .footer-bar {
    position: absolute;
    left: 0; right: 0; bottom: 0;
    height: 30px;
    background: var(--red);
    border-top: 3px solid var(--red-dark);
    color: var(--white);
    font-size: 9px;
    font-weight: 600;
    letter-spacing: 1px;
    display: flex;
    align-items: center;
    justify-content: center;
    gap: 6px;
  }
  .footer-bar .dot { width: 7px; height: 7px; border-radius: 50%; background: var(--white); }

  /* Back cover */
  .back-cover { background: var(--page-dark); }
  .fees-band {
    position: absolute;
    top: 40px; left: 0; right: 40px;
    background: var(--red);
    padding: 14px 20px;
    color: var(--white);
  }
  .fees-band h2 {
    font-size: 19px;
    font-weight: 700;
    line-height: 1.15;
    text-transform: uppercase;
  }
  .fees-band p {
    font-size: 8px;
    letter-spacing: 1px;
    text-transform: uppercase;
    margin-top: 5px;
  }
  .contact-list {
    position: absolute;
    top: 150px; left: 22px;
    list-style: none;
    color: var(--text-soft);
    font-size: 9px;
    line-height: 1.4;
  }
  .contact-list li { display: flex; align-items: flex-start; gap: 9px; margin-bottom: 9px; }
  .contact-list svg { flex: none; width: 14px; height: 14px; }
  .contact-list strong { color: var(--white); font-weight: 600; }
  .back-photo {
    position: absolute;
    left: 0; right: 0; top: 330px; bottom: 30px;
    background: linear-gradient(160deg, #1c2027 0%, #3a3b3d 45%, #15171b 100%);
  }

  /* Front cover */
  .front-cover { background: linear-gradient(180deg, #1b2636 0%, var(--page-navy) 100%); }
  .brand {
    position: absolute;
    top: 34px; left: 0; right: 0;
    text-align: center;
    color: var(--steel);
  }
  .brand .mark {
    display: block;
    width: 22px; height: 22px;
    margin: 0 auto 10px;
    background: var(--steel);
  }
  .brand .name {
    font-family: "Cinzel", Georgia, serif;
    font-size: 15px;
    font-weight: 700;
    letter-spacing: 1px;
    text-transform: uppercase;
  }
  .cover-photo {
    position: absolute;
    top: 110px; left: 0; right: 0; height: 300px;
    background: radial-gradient(ellipse at 50% 40%, #7fa6cf 0%, #2e4c70 40%, #0d1420 85%);
  }
  .cover-title {
    position: absolute;
    top: 420px; left: 0; right: 0;
    text-align: center;
    color: var(--white);
    font-family: "Cinzel", Georgia, serif;
    font-size: 24px;
    line-height: 1.2;
    text-transform: uppercase;
  }
  .cover-title .small { display: block; font-size: 15px; }

  /* Inside */
  .inside-left, .inside-right { background: var(--page-dark); }
  .inside-photo-top {
    position: absolute;
    top: 0; left: 0; right: 0; height: 300px;
    background: radial-gradient(ellipse at 45% 45%, #8a5a2a 0%, #3a2613 45%, #0e0c0a 90%);
  }
  .inside-photo-bottom {
    position: absolute;
    top: 270px; left: 0; right: 0; bottom: 30px;
    background: radial-gradient(ellipse at 50% 55%, #9fa7b3 0%, #4b5260 40%, #141820 90%);
  }
  .columns {
    position: absolute;
    left: 18px; right: 18px;
    display: flex;
    gap: 16px;
  }
  .inside-left .columns { top: 318px; }
  .inside-right .columns { top: 22px; }
  .service { flex: 1; }
  .service h3 {
    color: var(--orange);
    font-size: 13px;
    font-weight: 600;
    margin-bottom: 7px;
  }
  .service p {
    color: var(--text-body);
    font-size: 8px;
    line-height: 1.6;
  }
</style>
</head>
<body>

<section class="spread spread--outside">
  <div class="page back-cover">
    <div class="fees-band">
      <h2>Competitive Fees<br>for Investigative Services</h2>
      <p>In your face, objective information</p>
    </div>
    <ul class="contact-list">
      <li>
        <svg viewBox="0 0 14 14"><path d="M7 1a4 4 0 0 0-4 4c0 3 4 8 4 8s4-5 4-8a4 4 0 0 0-4-4zm0 5.5A1.5 1.5 0 1 1 7 3.5a1.5 1.5 0 0 1 0 3z" fill="#c41f2b"/></svg>
        <span><strong>Head Office</strong><br>1200 Harbor Street, Suite 4<br>Portland, OR 97201</span>
      </li>
      <li>
        <svg viewBox="0 0 14 14"><path d="M3 1.5l2.5 2.5-1.5 1.5a8 8 0 0 0 4.5 4.5l1.5-1.5 2.5 2.5-1.5 2C6 12.5 1.5 8 1 3z" fill="#c41f2b"/></svg>
        <span>Tel: 503 555 0142</span>
      </li>
      <li>
        <svg viewBox="0 0 14 14"><rect x="2" y="5" width="10" height="6" fill="#c41f2b"/><rect x="4" y="2" width="6" height="3" fill="#c41f2b"/></svg>
        <span>Fax: 503 555 0143</span>
      </li>
      <li>
        <svg viewBox="0 0 14 14"><rect x="1" y="3" width="12" height="8" fill="#c41f2b"/><path d="M1 3l6 5 6-5" stroke="#111318" fill="none"/></svg>
        <span>info@hallowaypartners.com</span>
      </li>
      <li>
        <svg viewBox="0 0 14 14"><circle cx="7" cy="7" r="5.5" stroke="#c41f2b" stroke-width="1.5" fill="none"/><path d="M1.5 7h11M7 1.5c-3 3-3 8 0 11M7 1.5c3 3 3 8 0 11" stroke="#c41f2b" fill="none"/></svg>
        <span>www.hallowaypartners.com</span>
      </li>
    </ul>
    <div class="back-photo" role="img" aria-label="Photograph of a dark city street at night"></div>
    <div class="footer-bar"><span class="dot"></span>WWW.HALLOWAYPARTNERS.COM</div>
  </div>

  <div class="page front-cover">
    <div class="brand">
      <span class="mark"></span>
      <span class="name">Halloway &amp; Partners Ltd.</span>
    </div>
    <div class="cover-photo" role="img" aria-label="Photograph of a silhouetted investigator standing in a lit doorway"></div>
    <h1 class="cover-title"><span class="small">Trusted,</span>Competent Information<br>and Evidence</h1>
    <div class="footer-bar"></div>
  </div>
</section>

<section class="spread spread--inside">
  <div class="page inside-left">
    <div class="inside-photo-top" role="img" aria-label="Photograph of a gloved hand holding handcuffs"></div>
    <div class="columns">
      <article class="service">
        <h3>Criminal Defense Investigation</h3>
        <p>We examine every detail of a case for the defense team. Our investigators locate witnesses, review police reports, revisit the scene and gather the facts that matter, so counsel can build a strong and informed strategy before trial.</p>
      </article>
      <article class="service">
        <h3>Civil Investigation</h3>
        <p>Halloway &amp; Partners supports attorneys and firms in civil matters of every size. We handle background checks, asset searches, surveillance and witness interviews, delivering clear findings that stand up to scrutiny and help clients resolve disputes with confidence.</p>
      </article>
    </div>
    <div class="footer-bar"><span class="dot"></span>WWW.HALLOWAYPARTNERS.COM</div>
  </div>

  <div class="page inside-right">
    <div class="columns">
      <article class="service">
        <h3>Information Services</h3>
        <p>As your trusted source of information, we gather and verify records quickly and discreetly. Whether you need a person located, a business checked or a history confirmed, our team delivers accurate reports you can act on without delay.</p>
      </article>
      <article class="service">
        <h3>Forensic Photography</h3>
        <p>Our forensic photography documents scenes, vehicles, injuries and property with precision. Every image is captured using proven methods, logged with care and prepared for court, giving you visual evidence that is clear, accurate and ready to present.</p>
      </article>
    </div>
    <div class="inside-photo-bottom" role="img" aria-label="Photograph of a damaged car at an accident scene at night"></div>
    <div class="footer-bar"><span class="dot"></span>WWW.HALLOWAYPARTNERS.COM</div>
  </div>
</section>

</body>
</html>
```